Birchwell Pantry Co - labels

I have my logo now so its time to proceed with the labels.
The product is organic juices and smoothies. They will be served in Mason jar's and sold as a premium hand made product into the CBD and outlets around Perth such as yoga studios gyms, cafe's etc. Cleanses to individuals etc.
I have attached the logo and a mock of what I would like to see.
I think the logo and the raw organic, handmade look will work with the Chalkboard design and maybe some bunting to brighten the design.
There is currently approx. 10 Juices and Smoothies to the range so I will need to settle on the design and then have you create a label for each one, once settled on the design.
If you have any questions please let me know.

Text on label:
Raw, Organic, Hand Made, Gluten-Free, Dairy-Free

Juice
Morning Tide Mix
Kale, Apple, Celery, Dandelion, Lemon & Ginger

This product is FRESH. Shake before you enjoy!!!

Label size. highest point for height 70 - 75mm. Length 200mm
I also have more wording and nutritional guide for Australian Standards. I will update soon.
Thank you

    Happy Friday Designers!!!

Well I have just increased the budget to $300. I hope this helps to get some designs coming through. If you need anything else from me please send a message.

I look forward to receiving your designs soon and thank you for working with me on my business. this is such an exciting time for me and you guys are making my dream a reality so thank you for your time.

Regards,

Denise

Reason: I have not received many designs so extending for a few more days.

• Wording - Hand Made
Raw, Organic, Gluten-Free, Dairy-Free
• A chalk board with Juice or Smoothie - Name and ingredients
Bunting I think will work well with the design of logo and chalk board plus bring some colour.

```html
<!DOCTYPE html>
<html lang="en">
<head>
<meta charset="utf-8">
<title>Birchwell Pantry Co – Juice Label</title>
<link rel="stylesheet" href="https://fonts.googleapis.com/css2?family=Bitter:wght@700;800&family=Damion&family=Shadows+Into+Light&display=swap">
<style>
  :root {
    --page: #f3f3f1;
    --band: #d9d9d9;
    --wood-light: #f4f4f3;
    --wood-mid: #e3e4e3;
    --wood-dark: #cfd1d0;
    --brand-green: #1fa85e;
    --leaf-green: #2fb36a;
    --bark-brown: #5a3d2b;
    --dot-brown: #6b4a35;
  }
  * { box-sizing: border-box; margin: 0; padding: 0; }
  html, body {
    width: 1200px;
    height: 900px;
    overflow: hidden;
    background: var(--page);
  }
  .label {
    position: absolute;
    left: 190px;
    top: 185px;
    width: 820px;
    height: 620px;
  }
  .label__wood {
    position: absolute;
    inset: 0;
    background:
      repeating-linear-gradient(90deg,
        var(--wood-light) 0 58px,
        var(--wood-dark) 58px 60px,
        var(--wood-mid) 60px 62px),
      var(--wood-light);
    opacity: 0.95;
  }
  .label__band {
    position: absolute;
    left: 0; top: 0;
    width: 100%;
    height: 26px;
    background: var(--band);
  }
  .brand {
    position: absolute;
    left: 246px;
    top: -87px;
    width: 324px;
    height: 324px;
    border-radius: 50%;
    background: var(--brand-green);
    display: flex;
    align-items: center;
    justify-content: center;
    text-align: center;
  }
  .brand__name {
    font-family: "Bitter", serif;
    font-weight: 800;
    font-size: 40px;
    line-height: 1.05;
    color: #e2e52a;
    width: 230px;
    text-transform: uppercase;
  }
  .claim {
    position: absolute;
    font-family: "Shadows Into Light", cursive;
    font-size: 30px;
    color: var(--leaf-green);
    white-space: nowrap;
    line-height: 1;
  }
  .product-name {
    position: absolute;
    left: 60px;
    top: 270px;
    width: 720px;
    text-align: center;
    font-family: "Damion", cursive;
    font-size: 96px;
    color: var(--bark-brown);
    line-height: 1.1;
    white-space: nowrap;
  }
  .star {
    position: absolute;
    left: 156px;
    top: 398px;
    width: 32px;
    height: 32px;
  }
  .category {
    position: absolute;
    left: 64px;
    top: 440px;
    font-family: "Bitter", serif;
    font-weight: 800;
    font-size: 96px;
    line-height: 1;
    color: var(--brand-green);
    letter-spacing: 1px;
  }
  .ingredients {
    position: absolute;
    left: 336px;
    top: 462px;
    display: grid;
    grid-template-columns: 122px 153px 120px;
    row-gap: 4px;
    list-style: none;
    font-family: "Bitter", serif;
    font-weight: 700;
    font-size: 25px;
    color: var(--bark-brown);
    line-height: 1.1;
  }
  .ingredients li::before {
    content: "•";
    color: var(--brand-green);
    margin-right: 6px;
  }
  .divider {
    position: absolute;
    left: 50px;
    top: 560px;
    width: 728px;
    border-top: 6px dotted var(--dot-brown);
  }
  .notice {
    position: absolute;
    left: 50px;
    top: 580px;
    width: 728px;
    text-align: center;
    font-family: "Bitter", serif;
    font-weight: 800;
    font-size: 22px;
    color: var(--bark-brown);
    text-transform: uppercase;
    white-space: nowrap;
    line-height: 1.2;
  }
  .notice__fresh {
    font-family: "Damion", cursive;
    font-weight: 400;
    font-size: 30px;
    color: var(--brand-green);
    text-transform: none;
  }
</style>
</head>
<body>
  <section class="label">
    <div class="label__wood" role="img" aria-label="Whitewashed wooden plank texture"></div>
    <div class="label__band"></div>

    <div class="brand">
      <span class="brand__name">Birchwell Pantry Co</span>
    </div>

    <p class="claim" style="left:44px; top:86px;">Handmade</p>
    <p class="claim" style="left:44px; top:138px;">Gluten-Free</p>
    <p class="claim" style="left:612px; top:80px;">Raw</p>
    <p class="claim" style="left:596px; top:140px;">Dairy-Free</p>
    <p class="claim" style="left:566px; top:196px;">Cold pressed</p>

    <h1 class="product-name">Morning Tide Mix</h1>

    <svg class="star" viewBox="0 0 24 24" aria-hidden="true">
      <polygon points="12,1 15,9 23,9 16.5,14 19,22 12,17 5,22 7.5,14 1,9 9,9" fill="#1fa85e"/>
    </svg>

    <h2 class="category">JUICE</h2>

    <ul class="ingredients">
      <li>Kale</li>
      <li>Celery</li>
      <li>Lemon</li>
      <li>Apple</li>
      <li>Dandeliona</li>
      <li>Ginger</li>
    </ul>

    <div class="divider"></div>

    <p class="notice">This product is <span class="notice__fresh">Fresh!</span> Shake before you enjoy!!!</p>
  </section>
</body>
</html>
```